Business card design needed

Just need something dynamic and unique
For a local painting contractor

Industry/Entity Type

Painting

Contact Information for Business Card

Carl Wexford
Painting Contactor
Interior & Exterior
New Work & Repaints
For an obligation free quote:
0498731046

```html
<!DOCTYPE html>
<html lang="en">
<head>
<meta charset="utf-8">
<title>Carl Wexford Painting Contactor – Business Card</title>
<link rel="stylesheet" href="https://fonts.googleapis.com/css2?family=Orbitron:wght@700;800&family=Didact+Gothic&display=swap">
<style>
  :root {
    --page-bg: #ffffff;
    --card-green: #9fcd55;
    --card-green-dark: #95c44c;
    --ink-emboss: #6c9d36;
    --ink-phone: #3b5721;
    --rule: #6c9d36;
    --highlight: rgba(255, 255, 255, 0.35);
    --lowlight: rgba(40, 70, 10, 0.35);
  }
  * { margin: 0; padding: 0; box-sizing: border-box; }
  html, body {
    width: 1200px;
    height: 900px;
    overflow: hidden;
    background: var(--page-bg);
  }
  .business-card {
    position: absolute;
    left: 60px;
    top: 116px;
    width: 1084px;
    height: 670px;
    background: linear-gradient(160deg, var(--card-green) 0%, var(--card-green-dark) 100%);
    box-shadow: 4px 6px 10px rgba(0, 0, 0, 0.35);
  }
  .card-line {
    position: absolute;
    left: 0;
    width: 100%;
    text-align: center;
    white-space: nowrap;
    color: var(--ink-emboss);
    font-family: "Orbitron", sans-serif;
    text-shadow: 1px 1px 0 var(--highlight), -1px -1px 0 var(--lowlight);
  }
  .owner-name {
    top: 96px;
    font-size: 64px;
    line-height: 68px;
    font-weight: 800;
    letter-spacing: 5px;
  }
  .trade-title {
    top: 166px;
    font-size: 64px;
    line-height: 68px;
    font-weight: 800;
    letter-spacing: 3px;
  }
  .service-scope {
    top: 292px;
    font-size: 40px;
    line-height: 44px;
    font-weight: 700;
    letter-spacing: 3px;
  }
  .service-detail {
    top: 382px;
    font-size: 25px;
    line-height: 28px;
    font-weight: 700;
    letter-spacing: 4px;
  }
  .divider {
    position: absolute;
    left: 50px;
    top: 466px;
    width: 984px;
    height: 5px;
    background: var(--rule);
    box-shadow: 1px 1px 0 var(--highlight);
  }
  .quote-line {
    top: 506px;
    font-family: "Didact Gothic", sans-serif;
    font-size: 58px;
    line-height: 68px;
    color: var(--ink-phone);
    text-shadow: none;
    letter-spacing: 1px;
  }
</style>
</head>
<body>
  <div class="business-card">
    <p class="card-line owner-name">CARL WEXFORD</p>
    <p class="card-line trade-title">PAINTING CONTACTOR</p>
    <p class="card-line service-scope">INTERIOR EXTERIOR</p>
    <p class="card-line service-detail">NEW WORK REPAINTS FOR AN OBLIGATION</p>
    <div class="divider"></div>
    <p class="card-line quote-line">Free quote: 0498731046</p>
  </div>
</body>
</html>
```